Radiant Crossing - An Exciting Mission & Book Cover Project

Help me to inspire people to live their best life! This is a mission, not just a design project.
I need a Book Cover designed to keep me inspired on the process of writing my book.
Book Title: Radiant Crossing
Tag Line: Three Simple Steps to get out of your own way, SuperCharge your Life and Step into Purpose!
Author: Marlis Quenby

The three steps are: Ownership, Vision and Action (Not sure if this should be on the front or back of the book cover)

The book is a self-help, motivational book. Personal development.
The cover needs to be strong and capture peoples attention, especially with competing shelf space. I almost see a fire ball of flame or explosion that will grab peoples attention.
My company is The Lantern Institute. I have added the company logo and a few pages of my presentation and topic outline to give an idea.
Maybe: The Lantern Institute logo on back of the cover. website is marlisquenby.com

THOUGHT: People should be able to take a photo of them holding the book cover showing what area of life they want Radiant Crossing in. This is why the front cover must be so visual and powerful that they want to take a photo with it. Ie. Explosion, fire, strong and bold.

Target Market(s)

Anyone who feels stuck and needs to breakthrough and move forward in life.

Industry/Entity Type

Motivation

Font styles to use
Serif
Sans Serif

Colors
ec1f27
f37122
fbed22

Requirements
Must have
• The design must be STRONG, SIMPLE, STAND OUT ON BOOK SHELVES.
Must have an open file to swap the photo and copy out.

Back Cover Page
1) Summary
2) 2-3 testimonials. One sentence.
3) About the Author (maybe with photo)
4) Lantern Institute logo
5) Website: radiantcrossing.com and marlisquenby.com
Nice to have
• If my photo works somewhere that would be great. I will change the photo later.
Added Where's Your Harbor? a nice cover example.
Should not have
• Right now I am writing the summary for the back of the cover. For now use Loreum Ipsum text and 2-3 recommendations. Again, I will get these only later.

```html
<!DOCTYPE html>
<html lang="en">
<head>
<meta charset="utf-8">
<title>Radiant Crossing – Book Cover</title>
<link href="https://fonts.googleapis.com/css2?family=Fira+Sans+Extra+Condensed:wght@400;700&family=PT+Sans:wght@400&display=swap" rel="stylesheet">
<style>
  :root {
    --stage: #e6eaee;
    --cover-red: #d0212b;
    --cover-red-deep: #b51b23;
    --title-red: #e01f27;
    --ink: #1c1414;
    --paper: #ffffff;
    --flame-yellow: #fbed22;
    --flame-orange: #f37122;
    --band-white: #f6f4f0;
    --cover-w: 450px;
    --cover-h: 760px;
  }
  * { box-sizing: border-box; margin: 0; padding: 0; }
  html, body {
    width: 1200px; height: 934px; overflow: hidden;
    background: var(--stage);
  }
  .spread {
    position: absolute; top: 87px; left: 140px;
    display: flex; gap: 20px;
  }
  .cover {
    position: relative; width: var(--cover-w); height: var(--cover-h);
    background: linear-gradient(100deg, var(--cover-red) 0%, var(--cover-red-deep) 100%);
    overflow: hidden;
    box-shadow: 0 10px 30px rgba(0,0,0,0.18);
  }

  /* Back cover */
  .summary {
    position: absolute; left: 74px; top: 106px; width: 341px;
    font: 400 9.6px/12.3px "PT Sans", sans-serif; color: var(--paper);
  }
  .author-photo {
    position: absolute; left: 74px; top: 277px; width: 85px; height: 113px;
    background: linear-gradient(180deg, #dcdcdc 0%, #b9b4ae 55%, #2b3550 100%);
  }
  .about {
    position: absolute; left: 166px; top: 276px; width: 249px;
    font: 400 9.6px/12.3px "PT Sans", sans-serif; color: var(--ink);
    text-align: justify;
  }
  .about h2 {
    font: 400 11px/14px "PT Sans", sans-serif; margin-bottom: 2px; text-align: left;
  }
  .imprint {
    position: absolute; right: 35px; top: 585px; width: 130px;
    display: flex; flex-direction: column; align-items: flex-start;
    font-family: "PT Sans", sans-serif; color: var(--ink);
  }
  .imprint-mark {
    width: 20px; height: 20px; border-radius: 50%;
    background: var(--flame-orange); align-self: center; margin-bottom: 10px;
  }
  .imprint-name { font-size: 11px; line-height: 13px; margin-bottom: 16px; }
  .imprint-web { font-size: 9.5px; line-height: 15px; color: var(--paper); }

  /* Front cover */
  .burst {
    position: absolute; left: 20px; top: 30px; width: 400px; height: 420px;
    background: radial-gradient(ellipse at 55% 40%, var(--flame-yellow) 0%, #f9c21e 30%, rgba(243,113,34,0.6) 55%, rgba(208,33,43,0) 72%);
  }
  .title-band {
    position: absolute; left: 63px; right: 0; top: 177px; height: 146px;
    background: linear-gradient(90deg, rgba(246,244,240,0) 0%, rgba(246,244,240,0.85) 35%, var(--band-white) 60%);
    border-bottom: 4px solid #7a0f12;
  }
  .title {
    position: absolute; right: 28px; top: 184px; text-align: right;
    font-family: "Fira Sans Extra Condensed", sans-serif; font-weight: 700;
    letter-spacing: -0.5px;
  }
  .title-top { display: block; color: var(--title-red); font-size: 60px; line-height: 60px; margin-right: 40px; }
  .title-bottom { display: block; color: var(--ink); font-size: 74px; line-height: 74px; }
  .steps { position: absolute; left: 0; top: 0; }
  .step-label {
    font-family: "Fira Sans Extra Condensed", sans-serif; font-size: 17px; fill: var(--ink);
  }
  .tagline {
    position: absolute; left: 40px; right: 28px; top: 535px; text-align: center;
    font: 400 25px/27px "Fira Sans Extra Condensed", sans-serif; color: var(--paper);
  }
  .author {
    position: absolute; right: 36px; top: 664px;
    font: 400 21px/24px "Fira Sans Extra Condensed", sans-serif; color: var(--ink);
  }
</style>
</head>
<body>
<main class="spread">
  <section class="cover cover-back">
    <p class="summary">Lorem ipsum dolor sit amet, consectetur adipiscing elit. Nunc rutrum mauris ultrices turpis malesuada rhoncus. Cras id orci ut tellus tincidunt imperdiet. Nullam efficitur pharetra interdum. Nullam turpis sem, aliquet et vestibulum quis, tempor sit amet mi. Nunc aliquam eget justo non placerat. Nunc dignissim cursus luctus. Pellentesque eget bibendum nisl, eu eleifend dolor. Pellentesque sed arcu ipsum. Phasellus at consequat sapien.<br>Ut ut metus sem. Vestibulum blandit augue id urna accumsan porttitor. Phasellus sit amet dolor faucibus, bibendum nisi vitae, consequat eros. Morbi tellus mauris, ultrices vel diam ut, cursus consequat justo. Pellentesque nec purus ac dolor iaculis iaculis. Morbi in metus porttitor, maximus urna vitae, dignissim nisl. Vivamus nec dignissim sem. Suspendisse mollis vel lorem non viverra. Suspendisse vel lectus auctor magna euismod rhoncus eget ac urna.</p>
    <div class="author-photo" role="img" aria-label="Portrait photo of the author"></div>
    <div class="about">
      <h2>About the Author</h2>
      <p>Hi, I'm Marlis. I've had an interesting life to say the least and I have learnt many lessons along the way. I have experienced the despair of rock bottom and have faced my fair share of demons. I never gave up and constantly chose to feed faith over fear. No matter what you may be going through, my message is simple. Everything you are facing is the perfect experience you need to have in order to grow and wake up. Challenges in your life are moulding and shaping your strength and character.</p>
    </div>
    <div class="imprint">
      <span class="imprint-mark"></span>
      <span class="imprint-name">The Lantern Institute</span>
      <span class="imprint-web">radiantcrossing.com</span>
      <span class="imprint-web">marlisquenby.com</span>
    </div>
  </section>

  <section class="cover cover-front">
    <div class="burst" role="img" aria-label="Bright yellow and orange explosion of light and sparks"></div>
    <div class="title-band"></div>
    <h1 class="title"><span class="title-top">Radiant</span><span class="title-bottom">Crossing</span></h1>
    <svg class="steps" width="450" height="760" viewBox="0 0 450 760" aria-label="Three steps: Ownership, Vision, Action">
      <defs>
        <linearGradient id="arrow-fill" x1="0" y1="0" x2="0" y2="1">
          <stop offset="0" stop-color="#f37122"/>
          <stop offset="1" stop-color="#fbd322"/>
        </linearGradient>
      </defs>
      <polygon points="110,323 175,323 175,410 193,410 142,475 92,410 110,410" fill="url(#arrow-fill)"/>
      <polygon points="197,323 262,323 262,370 279,370 229,428 180,370 197,370" fill="url(#arrow-fill)"/>
      <polygon points="283,323 348,323 348,408 361,408 313,472 266,408 283,408" fill="url(#arrow-fill)"/>
      <text class="step-label" x="142" y="436" text-anchor="middle">Ownership</text>
      <text class="step-label" x="229" y="390" text-anchor="middle">Vision</text>
      <text class="step-label" x="313" y="434" text-anchor="middle">Action</text>
    </svg>
    <p class="tagline">Three Simple Steps to get out of your own way<br>SuperCharge your Life and Step into Purpose!</p>
    <p class="author">Marlis Quenby</p>
  </section>
</main>
</body>
</html>
```